Course Graduation Certificate

This project is not for a flyer but instead for the creation of a course graduation certificate. The final certificate needs to include the Marlowe Summit Aviation Academy logo and the text stating as follows:
Certifies that ___________________________ has satisfactorily completed the course of _______________________________ on ________________________________
I would also like to include some type of gold seal of completion as well as a place to sign my name and credentials at the bottom of the certificate
I have included the Marlowe Summit Aviation Academy logo as well as three other certificate examples for you to work from.
Target Market(s)
Students completing a certification course and receiving a certificate
Look and feel

```html
<!DOCTYPE html>
<html lang="en">
<head>
<meta charset="utf-8">
<title>Course Graduation Certificate — Marlowe Summit Aviation Academy</title>
<link rel="stylesheet" href="https://fonts.googleapis.com/css2?family=Rokkitt:wght@300;400;500&display=swap">
<style>
  :root {
    --paper: #ffffff;
    --navy: #1f2a55;
    --gold: #c49a3a;
    --gold-light: #f1d58a;
    --gold-deep: #8a6418;
    --blue: #2f64c8;
    --blue-deep: #1d3f95;
    --blue-pale: #cfdcf3;
  }
  * { box-sizing: border-box; margin: 0; padding: 0; }
  html, body {
    width: 1200px; height: 848px; overflow: hidden; background: var(--paper);
  }
  .certificate {
    position: relative; width: 1200px; height: 848px; overflow: hidden;
    background: var(--paper);
    font-family: "Rokkitt", "Rockwell", serif;
    color: var(--navy);
  }
  .swoosh { position: absolute; inset: 0; width: 1200px; height: 848px; }
  .brand {
    position: absolute; top: 66px; right: 80px;
    display: flex; align-items: center; gap: 10px;
    font-weight: 500; font-size: 19px; letter-spacing: 2px;
    text-transform: uppercase; color: var(--blue-deep);
  }
  .brand-dot {
    width: 14px; height: 14px; border-radius: 50%; background: var(--blue-deep);
  }
  .title {
    position: absolute; top: 182px; left: 0; width: 1200px; padding-left: 196px;
    text-align: center; font-weight: 400; font-size: 86px;
    letter-spacing: 15px; color: var(--gold);
  }
  .line-text {
    position: absolute; font-weight: 400; font-size: 22px;
    letter-spacing: 4px; text-transform: uppercase; white-space: nowrap;
  }
  .certifies { top: 330px; left: 592px; }
  .recipient-line {
    position: absolute; top: 396px; left: 318px; width: 790px;
    border-top: 1.5px solid var(--navy);
  }
  .completed { top: 408px; left: 432px; }
  .course { top: 457px; left: 362px; display: flex; align-items: flex-end; }
  .date-on { top: 506px; left: 559px; display: flex; align-items: flex-end; }
  .blank {
    display: inline-block; border-bottom: 1.5px solid var(--navy);
    margin-left: 4px; margin-bottom: 6px;
  }
  .course .blank { width: 400px; }
  .date-on .blank { width: 262px; }
  .sign-label {
    position: absolute; top: 670px; font-weight: 500; font-size: 21px; letter-spacing: 1.5px;
  }
  .sign-date { left: 442px; }
  .sign-signature { left: 682px; }
  .seal { position: absolute; left: 912px; top: 575px; width: 200px; height: 200px; }
</style>
</head>
<body>
<main class="certificate">
  <svg class="swoosh" viewBox="0 0 1200 848" aria-hidden="true">
    <defs>
      <linearGradient id="blueBand" x1="0" y1="0" x2="1" y2="1">
        <stop offset="0" stop-color="var(--blue-deep)"/>
        <stop offset="0.45" stop-color="var(--blue)"/>
        <stop offset="1" stop-color="var(--blue-deep)"/>
      </linearGradient>
      <linearGradient id="goldBand" x1="0" y1="0" x2="1" y2="0">
        <stop offset="0" stop-color="var(--gold-deep)"/>
        <stop offset="0.4" stop-color="var(--gold-light)"/>
        <stop offset="0.7" stop-color="var(--gold)"/>
        <stop offset="1" stop-color="var(--gold-deep)"/>
      </linearGradient>
      <radialGradient id="sheen" cx="0.15" cy="0.7" r="0.6">
        <stop offset="0" stop-color="#ffffff"/>
        <stop offset="1" stop-color="#ffffff" stop-opacity="0"/>
      </radialGradient>
    </defs>
    <path d="M0 0 H330 C190 170 150 520 360 848 H0 Z" fill="url(#blueBand)"/>
    <path d="M0 230 C60 420 140 640 300 848 H0 Z" fill="var(--blue-pale)"/>
    <path d="M0 330 C40 520 100 700 220 848 H0 Z" fill="url(#sheen)"/>
    <path d="M95 0 H158 C110 140 105 330 150 520 C190 680 260 780 340 848 H290 C190 770 100 640 70 470 C45 300 60 120 95 0 Z" fill="url(#goldBand)"/>
    <path d="M0 640 C60 740 120 800 190 848" fill="none" stroke="var(--gold)" stroke-width="4"/>
    <path d="M0 690 C45 760 90 810 140 848" fill="none" stroke="var(--blue-deep)" stroke-width="10"/>
  </svg>

  <div class="brand"><span class="brand-dot"></span>Marlowe Summit Aviation Academy</div>

  <h1 class="title">CERTIFICATE</h1>

  <p class="line-text certifies">Certifies that</p>
  <div class="recipient-line"></div>
  <p class="line-text completed">Has satisfactorily completed</p>
  <p class="line-text course">The course of<span class="blank"></span></p>
  <p class="line-text date-on">On<span class="blank"></span></p>

  <p class="sign-label sign-date">DATE</p>
  <p class="sign-label sign-signature">SIGNATURE</p>

  <svg class="seal" viewBox="0 0 200 200" role="img" aria-label="Gold seal of completion">
    <defs>
      <radialGradient id="sealGold" cx="0.4" cy="0.35" r="0.75">
        <stop offset="0" stop-color="var(--gold-light)"/>
        <stop offset="0.55" stop-color="var(--gold)"/>
        <stop offset="1" stop-color="var(--gold-deep)"/>
      </radialGradient>
      <filter id="sealShadow" x="-20%" y="-20%" width="150%" height="150%">
        <feDropShadow dx="6" dy="8" stdDeviation="6" flood-color="#000" flood-opacity="0.35"/>
      </filter>
    </defs>
    <circle cx="98" cy="97" r="88" fill="url(#sealGold)" stroke="var(--gold-deep)" stroke-width="6" stroke-dasharray="6 5" filter="url(#sealShadow)"/>
    <circle cx="98" cy="97" r="70" fill="none" stroke="var(--gold-deep)" stroke-width="1.5" opacity="0.6"/>
  </svg>
</main>
</body>
</html>
```